Solar Energy in Panama- Vantoro Home Kits

We will need a catalog which explains Our company, how Vantoro Home Kit works, and give technical especifications and benefits of each size of Vantoro Home Kit in Spanish.
It needs to use same design as Video, and Website.
http://www.brisaluma.org/vantoro-home-kit.html
https://www.clipvesta.net/watch?v=Tq7LmRw2ZpA

It needs to have all products specificied in the powerpoint at the end.

Target Market(s)

Panama Country, home owners and business owners.

Industry/Entity Type

Solar Energy

Font styles to use
Sans Serif

Colors
9bcb3c
33a6d7
ffffff

Requirements
Must have
• It needs to use same design as Video, and Website.
• http://www.brisaluma.org/vantoro-home-kit.html
• https://www.clipvesta.net/watch?v=Tq7LmRw2ZpA
• It needs to have all products specificied in the powerpoint at the end.

```html
<!DOCTYPE html>
<html lang="es">
<head>
<meta charset="utf-8">
<title>Brisaluma – Catálogo Vantoro Home Kits</title>
<link href="https://fonts.googleapis.com/css2?family=Montserrat:wght@400;600;700;800&family=Open+Sans:wght@400;600;700&display=swap" rel="stylesheet">
<style>
:root{
  --green:#9bcb3c;
  --green-dark:#6fa82a;
  --blue:#33a6d7;
  --navy:#1a6da6;
  --white:#ffffff;
  --ink:#4b4f54;
  --muted:#7d8389;
  --bg:#e9ebed;
  --head-grad:linear-gradient(90deg,#d9ecb4 0%,#e6f2f5 55%,#cde7f3 100%);
}
*{box-sizing:border-box;margin:0;padding:0}
html,body{width:1200px;height:831px;overflow:hidden;background:var(--bg)}
body{font-family:"Open Sans",Arial,sans-serif;color:var(--ink);position:relative}
.spread{position:absolute;width:540px;height:382px;display:flex;box-shadow:0 2px 8px rgba(0,0,0,.18)}
.s1{left:40px;top:22px}.s2{left:620px;top:22px}.s3{left:40px;top:427px}.s4{left:620px;top:427px}
.page{position:relative;width:270px;height:382px;background:var(--white);overflow:hidden}
.page+.page{border-left:1px solid #e2e4e6}
.head-band{position:absolute;left:0;top:0;width:100%;height:34px;background:var(--head-grad)}
.head-band svg{position:absolute;left:0;bottom:-1px;width:100%;height:14px}
.foot{position:absolute;left:0;bottom:0;width:100%;height:42px}
.ph{position:absolute;display:flex;align-items:flex-end}
.h{font-family:"Montserrat",Arial,sans-serif;font-weight:700;color:var(--blue);font-size:8.5px;line-height:1.2}
.p{font-size:4.6px;line-height:1.45;color:var(--ink)}
.p b{color:#333}
.ul{list-style:none}
.ul li{font-size:4.6px;line-height:1.45;margin-bottom:2.5px;padding-left:5px;position:relative}
.ul li::before{content:"";position:absolute;left:0;top:2px;width:2px;height:2px;border-radius:50%;background:var(--blue)}
.brand{position:absolute;display:flex;align-items:center;gap:4px;font-family:"Montserrat",Arial,sans-serif;font-weight:800;color:var(--green-dark);letter-spacing:-.3px}
.brand i{display:block;background:var(--blue);border-radius:50%}
.brand-sub{position:absolute;font-family:"Montserrat",Arial,sans-serif;font-size:5px;letter-spacing:1.2px;color:var(--muted)}
.tag{display:inline-block;background:var(--green);color:var(--white);font-family:"Montserrat",Arial,sans-serif;font-weight:700;font-size:4.4px;padding:1.5px 5px;border-radius:2px}
.cap{position:absolute;background:var(--green);color:var(--white);font-size:4.2px;font-weight:700;text-align:center;padding:2px 3px;border-radius:2px}
.url{font-family:"Montserrat",Arial,sans-serif;font-weight:700;color:var(--green);letter-spacing:1px}

/* cover */
.cover-photo{left:0;top:60px;width:270px;height:190px;background:linear-gradient(180deg,#d7e6ef 0%,#a9c4d6 45%,#5d8bb0 70%,#1f4f8a 100%)}
.cover-blue{position:absolute;left:0;top:232px;width:100%;height:150px}
.cover-text{position:absolute;left:30px;right:30px;top:292px;text-align:center;color:var(--white);font-size:6.3px;line-height:1.45}
.cover-url{position:absolute;left:0;right:0;top:336px;text-align:center;font-size:7.5px}

/* product grid */
.prod{position:absolute;width:112px}
.prod .box{height:44px;background:linear-gradient(135deg,#f2f2f2,#c9ccd0);border-radius:2px}
.prod .spec{font-size:4px;line-height:1.4;margin-top:4px}
.prod .spec b{color:#333}
.price-row{display:flex;justify-content:flex-end;margin-top:3px}
.price{background:var(--green);color:var(--white);font-size:3.8px;font-weight:700;padding:2px 5px;border-radius:5px;text-align:center;line-height:1.2}
.step{position:absolute;left:14px;right:14px;display:flex;gap:6px}
.step .tag{flex:0 0 auto;height:8px}
.step p{font-size:4.4px;line-height:1.45}
</style>
</head>
<body>

<svg width="0" height="0" style="position:absolute" aria-hidden="true">
  <defs>
    <symbol id="foot-wave" viewBox="0 0 270 42" preserveAspectRatio="none">
      <path d="M0 16 C70 2 160 30 270 8 L270 42 L0 42 Z" fill="#9bcb3c"/>
      <path d="M0 24 C80 10 170 36 270 18 L270 42 L0 42 Z" fill="#33a6d7"/>
      <path d="M0 34 C90 24 180 42 270 30 L270 42 L0 42 Z" fill="#1a6da6"/>
    </symbol>
    <symbol id="head-wave" viewBox="0 0 270 14" preserveAspectRatio="none">
      <path d="M0 8 C90 0 180 14 270 4 L270 14 L0 14 Z" fill="#ffffff"/>
    </symbol>
  </defs>
</svg>

<!-- Spread 1: cover + company letter -->
<section class="spread s1">
  <div class="page cover">
    <div class="brand" style="left:36px;top:24px;font-size:19px"><i style="width:9px;height:9px"></i>Brisaluma</div>
    <div class="brand-sub" style="left:52px;top:47px">SOLUCIONES SOLARES</div>
    <div class="ph cover-photo" role="img" aria-label="Fotografía del skyline de Ciudad de Panamá sobre paneles solares"></div>
    <svg class="cover-blue" viewBox="0 0 270 150" preserveAspectRatio="none">
      <path d="M0 30 C90 0 180 50 270 14 L270 150 L0 150 Z" fill="#9bcb3c"/>
      <path d="M0 44 C90 18 180 62 270 30 L270 150 L0 150 Z" fill="#33a6d7"/>
      <path d="M0 130 C90 118 180 146 270 124 L270 150 L0 150 Z" fill="#1a6da6"/>
    </svg>
    <p class="cover-text">Panamá ha firmado un compromiso para apoyar las fuentes de energía renovables, ya que actualmente solo el 5% de la electricidad que consumimos es limpia.</p>
    <p class="url cover-url">WWW.BRISALUMA.ORG</p>
  </div>
  <div class="page">
    <div style="position:absolute;left:18px;top:22px;width:112px">
      <p class="p">Solvaro Soluciones Inc., miembro de la Asociación Istmeña de Energía Limpia, se dedica a ofrecer tecnología solar accesible para hogares y negocios en todo el país. Nuestro equipo instala sistemas conectados a la red con garantía y soporte local.</p>
      <p class="p" style="margin-top:5px">Gracias a estos sistemas conectados a la red, el cliente genera su propia electricidad durante el día y reduce de forma directa su factura mensual con la distribuidora.</p>
      <p class="p" style="margin-top:5px">Ofrecemos asesoría, diseño, instalación y monitoreo del sistema, y acompañamos al cliente en cada permiso necesario ante la distribuidora.</p>
    </div>
    <div style="position:absolute;left:142px;top:22px;width:112px">
      <p class="p">Es necesario mencionar que cada sistema es diseñado según el consumo real del hogar o negocio, y que su inversión se recupera en pocos años.</p>
    </div>
    <div class="ph" role="img" aria-label="Fotografía del kit: paneles, microinversores, caja y soportes" style="left:146px;top:78px;width:108px;height:88px;background:linear-gradient(135deg,#eef1f4,#b9c2cb)"></div>
    <div class="brand" style="left:150px;top:182px;font-size:13px"><i style="width:6px;height:6px"></i>Brisaluma</div>
    <div class="brand-sub" style="left:162px;top:199px;font-size:4px">SOLUCIONES SOLARES</div>
    <div style="position:absolute;left:0;top:238px;width:100%;height:144px;background:linear-gradient(180deg,#33a6d7,#1a6da6)"></div>
    <svg style="position:absolute;left:0;top:226px;width:100%;height:24px" viewBox="0 0 270 24" preserveAspectRatio="none"><path d="M0 10 C90 0 180 20 270 6 L270 24 L0 24 Z" fill="#9bcb3c"/><path d="M0 16 C90 6 180 26 270 12 L270 24 L0 24 Z" fill="#33a6d7"/></svg>
    <div style="position:absolute;left:18px;top:258px;width:112px" class="p">
      <p style="color:#fff"><b style="color:#fff">Vantoro Home Kit</b><br>Sistema solar completo para su techo, listo para conectarse a la red eléctrica de su hogar y comenzar a ahorrar desde el primer día.</p>
    </div>
    <div style="position:absolute;left:146px;top:258px;width:110px;color:#fff;font-size:4.8px;line-height:1.5">
      Atentamente<br><b>Ing. Lucía Marenco</b><br>Directora de Ventas<br>SOLVARO SOLUCIONES INC.<br>Cel: 6123-4587
    </div>
    <p class="url" style="position:absolute;left:0;right:0;top:350px;text-align:center;font-size:6px">WWW.BRISALUMA.ORG</p>
  </div>
</section>

<!-- Spread 2: system types + kit contents -->
<section class="spread s2">
  <div class="page">
    <div class="ph" role="img" aria-label="Fotografía de paneles solares sobre un techo con árboles al fondo" style="left:0;top:0;width:270px;height:96px;background:linear-gradient(160deg,#dfe9f1 0%,#4f7fb6 50%,#6aa04a 100%)"></div>
    <svg style="position:absolute;left:0;top:86px;width:100%;height:14px"><use href="#head-wave"/></svg>
    <h2 class="h" style="position:absolute;left:14px;top:106px;width:112px">¿Qué tipo de Sistema Solar para mí?</h2>
    <div style="position:absolute;left:14px;top:130px;width:112px">
      <p class="p">Actualmente en el mercado hay diferentes tipos de sistemas solares. Tipo de conexión o almacenamiento de la electricidad:</p>
      <p class="p" style="margin-top:4px"><b>a. On Grid:</b> que son los que están conectados a la red eléctrica; este tipo es ideal para las ciudades y lugares urbanizados donde se cuenta con red eléctrica y contrato con la distribuidora de luz (ENDESUR o Naturelec). Las ventajas de este tipo: es contar con un menor costo y ser más ecológico ya que no necesitas baterías.</p>
      <p class="p" style="margin-top:4px"><b>b. Off Grid:</b> no están conectados a la red eléctrica. Se utilizan baterías para almacenar la electricidad. Este tipo es ideal para lugares rurales, fincas, invernaderos, hoteles y cabañas donde no se cuenta con red eléctrica.</p>
    </div>
    <h2 class="h" style="position:absolute;left:140px;top:106px;width:118px">¿Qué Capacidad de Sistema Solar necesito?</h2>
    <div style="position:absolute;left:140px;top:130px;width:118px">
      <p class="p">El sistema de Vantoro Home Kit con microinversores es la mejor manera de empezar con el uso de energía solar. El tamaño mínimo del sistema son 2kW, cuenta con 8 paneles solares de 250W, que no le quitarán mucho espacio del techo, pero la energía que producen puede alimentar o reducir el gasto de electricidad de aparatos pequeños como luz, televisión y algunos aparatos de cocina. El mismo produce entre 250-300 kWh mensuales, que es lo que un hogar conservativo en electricidad gasta. El promedio de los panameños gasta 600 kWh al mes; basado en este promedio, el mismo podría generar 50% de ahorro de energía.</p>
    </div>
    <div class="ph" role="img" aria-label="Ilustración técnica de una casa con paneles solares, microinversores y conexión a la red" style="left:118px;top:248px;width:140px;height:92px;background:linear-gradient(180deg,#eef4f7,#c8d9b8)"></div>
    <div class="brand" style="left:14px;top:268px;font-size:10px"><i style="width:5px;height:5px"></i>Brisaluma</div>
    <div class="brand-sub" style="left:22px;top:282px;font-size:3.6px">SOLUCIONES SOLARES</div>
    <svg class="foot"><use href="#foot-wave"/></svg>
  </div>
  <div class="page">
    <div class="head-band"><svg><use href="#head-wave"/></svg></div>
    <h2 class="h" style="position:absolute;left:14px;top:40px">¿Qué incluye este Vantoro Home Kit?</h2>
    <p class="p" style="position:absolute;left:14px;top:54px;width:240px">Nuestros kits brindan todos los componentes necesarios de principio a fin.</p>
    <div class="ph" role="img" aria-label="Foto de paneles solares" style="left:14px;top:68px;width:70px;height:64px;background:linear-gradient(135deg,#dff0f8,#2d4f86)"></div>
    <div class="ph" role="img" aria-label="Foto de microinversor" style="left:96px;top:68px;width:70px;height:64px;background:linear-gradient(135deg,#dff0f8,#4a4f55)"></div>
    <div class="ph" role="img" aria-label="Foto de soportes de techo" style="left:178px;top:68px;width:70px;height:64px;background:linear-gradient(135deg,#dff0f8,#9aa1a8)"></div>
    <span class="cap" style="left:27px;top:126px;width:44px">Paneles Solares</span>
    <span class="cap" style="left:109px;top:126px;width:44px">Micro Inversores</span>
    <span class="cap" style="left:191px;top:126px;width:44px">Soportes de techo</span>
    <div style="position:absolute;left:14px;top:144px;width:240px">
      <p class="h" style="font-size:5.6px">Paneles Solares</p>
      <p class="p">Alto rendimiento con 60 celdas policristalinas con 25 años de garantía.</p>
      <p class="h" style="font-size:5.6px;margin-top:4px">Micro Inverters</p>
      <p class="p">Micro inversores con sistema Voltiq que se conecta a cada uno a 2 paneles solares.</p>
      <p class="h" style="font-size:5.6px;margin-top:4px">Soportes y piezas de agarre</p>
      <p class="p">Molduras de acero para que puedas colocar los paneles en el techo.</p>
      <ul class="ul" style="margin-top:5px;padding-left:8px">
        <li>Sistema de monitoreo – Gratis con cada kit para que puedas analizar la producción de electricidad de su sistema en tiempo real.</li>
        <li>Sistema de diseño y de análisis financiero – Con el mismo puedes calcular el retorno de inversión de su sistema solar.</li>
        <li>Cableado adicional, conectores, interruptores, caja de conexiones.</li>
      </ul>
    </div>
    <div class="ph" role="img" aria-label="Ilustración de una mujer señalando hacia el texto" style="left:14px;top:248px;width:70px;height:100px;background:linear-gradient(180deg,#f4f6f8,#d5dde4)"></div>
    <div class="brand" style="left:104px;top:262px;font-size:19px"><i style="width:8px;height:8px"></i>Brisaluma</div>
    <p class="p" style="position:absolute;left:110px;top:296px;width:130px;text-align:center;font-size:5px">Panamá ha firmado un compromiso para apoyar las fuentes de energía renovables, ya que actualmente solo el 5% de la electricidad que consumimos es limpia.</p>
    <svg class="foot"><use href="#foot-wave"/></svg>
  </div>
</section>

<!-- Spread 3: micro inverters + monitoring -->
<section class="spread s3">
  <div class="page">
    <div class="head-band"><svg><use href="#head-wave"/></svg></div>
    <h2 class="h" style="position:absolute;left:14px;top:40px">¿Por qué los Micro Inversores son mejores?</h2>
    <div class="ph" role="img" aria-label="Diagrama comparativo: sistema con inversor centralizado frente a sistema con microinversores bajo sombra" style="left:14px;top:56px;width:242px;height:80px;background:linear-gradient(90deg,#e9edf1,#f3e1c8)"></div>
    <p class="p" style="position:absolute;left:40px;top:140px;width:190px;text-align:center;font-size:4.2px">En un sistema centralizado, una pequeña sombra en un panel reduce la producción de toda la cadena de paneles.</p>
    <div style="position:absolute;left:14px;top:158px;width:242px">
      <p class="p"><b>Mayor Seguridad:</b> El sistema no utiliza voltajes directos o DC, eliminando el riesgo de posibles incendios. El sistema de cableado a través del techo hasta el interruptor es de un voltaje regular de 240V AC, es el mismo que cualquier otro tipo de cableado de casa, y el circuito es protegido por el interruptor del panel principal.</p>
      <p class="p" style="margin-top:5px"><b>Mayor eficiencia sin tolerancia de sombras.</b> Cada panel solar opera independientemente, ya que cada panel tiene su propio micro inversor. Gracias a esto el sistema no sufre impacto si la obstrucción o sombra en uno, y su bajo desempeño no afecta el resto de los paneles, como explicamos con la imagen de arriba. En un sistema regular con inversor central la generación de corriente directa, todos los paneles se ven afectados si uno se encuentra bloqueado sin recibir luz solar.</p>
      <p class="p" style="margin-top:5px"><b>Fácilmente expandible:</b> El tamaño del sistema no está limitado por el tamaño de su inversión, ya que usted puede incrementar la cantidad de paneles de uno en uno hasta que su techo, espacio o presupuesto lo permita.</p>
    </div>
    <div class="ph" role="img" aria-label="Foto de un microinversor con cables" style="left:20px;top:270px;width:90px;height:50px;background:linear-gradient(135deg,#f1f2f3,#3e4348)"></div>
    <p class="p" style="position:absolute;left:128px;top:272px;width:124px">Los micro inversores son de alta calidad y tienen garantía hasta por 10 años. Comuníquese ahora para darnos los detalles de su consumo de electricidad y le podemos proporcionar un estimado de qué capacidad de kit requiere.</p>
    <svg class="foot"><use href="#foot-wave"/></svg>
  </div>
  <div class="page">
    <div class="head-band"><svg><use href="#head-wave"/></svg></div>
    <h2 class="h" style="position:absolute;left:14px;top:40px">Sistema de monitoreo incluido.</h2>
    <p class="p" style="position:absolute;left:14px;top:54px;width:240px">Todos nuestros Vantoro Home Kits incluyen sistema de monitoreo de cada micro inversor, con el mismo usted puede monitorear en tiempo real la eficiencia y generación de electricidad de cada uno.</p>
    <div class="ph" role="img" aria-label="Foto del comunicador de monitoreo con antena" style="left:20px;top:76px;width:100px;height:70px;background:linear-gradient(180deg,#e4f3fa,#b6dcee)"></div>
    <div class="ph" role="img" aria-label="Foto de una laptop mostrando el panel de monitoreo" style="left:146px;top:76px;width:100px;height:70px;background:linear-gradient(180deg,#e4f3fa,#b6dcee)"></div>
    <span class="cap" style="left:36px;top:140px;width:68px">Voltiq Systems<br>Communicator (ECU)</span>
    <span class="cap" style="left:162px;top:140px;width:68px">Voltiq Systems<br>Monitor (EMA)</span>
    <h2 class="h" style="position:absolute;left:14px;top:170px">¿Qué tan fácil es la instalación?</h2>
    <ul class="ul" style="position:absolute;left:14px;top:186px;width:128px">
      <li>Un sistema solar de 2kW toma en instalarse 1 fin de semana o 2 días.</li>
      <li>Nuestros kit utilizan paneles, inversores, soportes de techo de fácil instalación, cada uno viene con su manual de cómo se debe instalar.</li>
      <li>Un propietario que se siente cómodo trabajando en el techo de su casa, lo puede hacer fácilmente.</li>
      <li>Los micro inversores es lo último en seguridad, ya que los paneles directamente generan energía AC, en vez de la peligrosa corriente DC.</li>
      <li>Los micro inversores también le permiten ir agregando la cantidad de paneles que necesites para expandir su sistema solar en el futuro. Como cada panel es independiente puedes incrementar el 25% del sistema tan solo con un panel extra.</li>
      <li>En caso de lo requiera, nosotros le podemos poner en contacto con nuestro socio en instalación.</li>
    </ul>
    <div class="ph" role="img" aria-label="Fotografía de un técnico instalando paneles solares en un techo" style="left:150px;top:180px;width:110px;height:150px;background:linear-gradient(160deg,#c9def0 0%,#3a65a3 55%,#8a5a44 100%)"></div>
    <svg class="foot"><use href="#foot-wave"/></svg>
  </div>
</section>

<!-- Spread 4: installation steps + products -->
<section class="spread s4">
  <div class="page">
    <div class="head-band"><svg><use href="#head-wave"/></svg></div>
    <h2 class="h" style="position:absolute;left:14px;top:40px">¿Cuál es el proceso de instalación?</h2>
    <div class="step" style="top:58px"><span class="tag">Step 1</span><p>Instalar un Vantoro Home Kit de 2kW toma 2 días o un fin de semana una vez tenga los permisos necesarios para su instalación. Los permisos los detallamos abajo:<br>a. Entregar una nota a la distribuidora indicando que desea conectarse a las redes de la misma, y adjuntar:<br>&nbsp;&nbsp;i. Diseño eléctrico de la instalación de la Central Particular, debidamente aprobado por las autoridades competentes.<br>&nbsp;&nbsp;ii. Capacidad de la Central Particular en kW y las características técnicas de la misma.<br>&nbsp;&nbsp;iii. Especificaciones técnicas de todos los equipos que conforman la Central Particular. La distribuidora tiene 30 días para contestar y se firmará el acuerdo de interconexión.</p></div>
    <div class="step" style="top:140px"><span class="tag">Step 2</span><p>Una vez firmado el acuerdo, se procede con la instalación de sus equipos; los soportes de techo para los paneles deben ser instalados; este es el paso más laborioso de la instalación solar.</p></div>
    <div class="step" style="top:166px"><span class="tag">Step 3</span><p>Una vez que el sistema de montaje está en su techo, los paneles solares y los inversores se pueden instalar rápidamente. El o los inversores deben conectarse a los paneles en serie y después los mismos deben conectarse a la red eléctrica.</p></div>
    <div class="step" style="top:192px"><span class="tag">Step 4</span><p>Cuando la instalación se haya completado, un inspector de la distribuidora tiene que hacer pruebas, firmar y dar su aprobación. Usted puede lograr esto mediante la programación de una reunión de inspección.</p></div>
    <div class="step" style="top:218px"><span class="tag">Step 5</span><p>Una vez que se reciba la notificación escrita de aprobación por parte de la distribuidora, la que deberá ser emitida en un plazo no mayor de diez días calendario, usted puede hacer uso de su sistema solar.</p></div>
    <div class="step" style="top:244px"><span class="tag">Step 6</span><p>Nuestro trabajo no ha terminado hasta que su sistema esté produciendo energía limpia del sol. Le ofrecemos asistencia durante todo el proceso de instalación con los manuales, videos y soporte técnico.</p></div>
    <div class="ph" role="img" aria-label="Fotografía de paneles solares con la ciudad de Panamá al fondo" style="left:0;top:290px;width:270px;height:92px;background:linear-gradient(180deg,#dbe8f1 0%,#7fa3c5 50%,#2a4f8a 100%)"></div>
    <svg class="foot"><use href="#foot-wave"/></svg>
  </div>
  <div class="page">
    <div class="head-band"><svg><use href="#head-wave"/></svg></div>
    <h2 class="h" style="position:absolute;left:14px;top:40px">Products</h2>

    <div class="prod" style="left:14px;top:54px">
      <div class="box" role="img" aria-label="Caja del producto Vantoro Home Kit 2000 W"></div>
      <p class="spec"><b>Consumo mensual:</b> 250 kWh a 300 kWh<br><b>Espacio:</b> 16 m2<br><b>Paneles:</b> 8 paneles solares<br><b>Micro Inversores:</b> 4 (uno por cada 2 paneles)<br><b>Piezas de soporte:</b> barras de acero con molduras<br><b>Sistema de monitoreo:</b> gratis con cada kit<br><b>Diseño y análisis financiero</b> incluido<br><b>Otros:</b> cableado, conectores, caja.</p>
      <div class="price-row"><span class="price">Ahorro anual: $480<br>Ahorro mensual: $40</span></div>
    </div>
    <div class="prod" style="left:144px;top:54px">
      <div class="box" role="img" aria-label="Caja del producto Vantoro Home Kit 3000 W"></div>
      <p class="spec"><b>Consumo mensual:</b> 375 kWh a 450 kWh<br><b>Espacio:</b> 24 m2<br><b>Paneles:</b> 12 paneles solares<br><b>Micro Inversores:</b> 6 (uno por cada 2 paneles)<br><b>Piezas de soporte:</b> barras de acero con molduras<br><b>Sistema de monitoreo:</b> gratis con cada kit<br><b>Diseño y análisis financiero</b> incluido<br><b>Otros:</b> cableado, conectores, caja.</p>
      <div class="price-row"><span class="price">Ahorro anual: $720<br>Ahorro mensual: $60</span></div>
    </div>
    <div class="prod" style="left:14px;top:190px">
      <div class="box" role="img" aria-label="Caja del producto Vantoro Home Kit 4000 W"></div>
      <p class="spec"><b>Consumo mensual:</b> 500 kWh a 600 kWh<br><b>Espacio:</b> 32 m2<br><b>Paneles:</b> 16 paneles solares<br><b>Micro Inversores:</b> 8 (uno por cada 2 paneles)<br><b>Piezas de soporte:</b> barras de acero con molduras<br><b>Sistema de monitoreo:</b> gratis con cada kit<br><b>Diseño y análisis financiero</b> incluido<br><b>Otros:</b> cableado, conectores, caja.</p>
      <div class="price-row"><span class="price">Ahorro anual: $960<br>Ahorro mensual: $80</span></div>
    </div>
    <div class="prod" style="left:144px;top:190px">
      <div class="box" role="img" aria-label="Caja del producto Vantoro Home Kit 5000 W"></div>
      <p class="spec"><b>Consumo mensual:</b> 625 kWh a 750 kWh<br><b>Espacio:</b> 40 m2<br><b>Paneles:</b> 20 paneles solares<br><b>Micro Inversores:</b> 10 (uno por cada 2 paneles)<br><b>Piezas de soporte:</b> barras de acero con molduras<br><b>Sistema de monitoreo:</b> gratis con cada kit<br><b>Diseño y análisis financiero</b> incluido<br><b>Otros:</b> cableado, conectores, caja.</p>
      <div class="price-row"><span class="price">Ahorro anual: $1200<br>Ahorro mensual: $100</span></div>
    </div>
    <svg class="foot"><use href="#foot-wave"/></svg>
  </div>
</section>

</body>
</html>
```